Business Card Design with existing logo

TealHeron provides inspirational leadership training and coaching for corporate executives. We focus on being challenging, humorous and compassionate, providing the right mix of support and push for individuals and teams to improve their knowledge and performance. The colour purple is essential to the design. We already have a logo we are very happy with - we are curious to see what can be done to come across in a professional, high standard way that sets us apart. Ideally the design should include the photo of Lise-Britt
Target Market(s)
HR/ Senior Management 500 - 1500 employees
Industry/Entity Type
Leadership
Contact Information for Business Card
TealHeron Coaching Ltd
Inspirational leadership
Lise-Britt Holmgaard Pennick
Leadership coach and trainer
Telephone: +44 1632 960 418
Mobile: +44 7700 900 562
e-mail: lisebritt@tealheroncoaching.example
www.tealheroncoaching.example
Requirements
Must have
- The existing logo
Picture of Lise-Britt

```html
<!DOCTYPE html>
<html lang="en">
<head>
<meta charset="utf-8">
<title>TealHeron Coaching – Business Card</title>
<link rel="stylesheet" href="https://fonts.googleapis.com/css2?family=Crimson+Text:wght@400;600&display=swap">
<style>
  :root {
    --backdrop: #e6e6e8;
    --card: #ffffff;
    --purple: #6a3d96;
    --purple-band: #7a4aa8;
    --ink: #3d3d3f;
    --muted: #6b6b6e;
    --rule: #9a9a9d;
    --photo-light: #d9d9d9;
    --photo-dark: #6f6f6f;
  }
  * { box-sizing: border-box; margin: 0; padding: 0; }
  html, body {
    width: 1200px; height: 437px; overflow: hidden;
    background: var(--backdrop);
    font-family: "Crimson Text", Georgia, serif;
    color: var(--ink);
  }
  .canvas { position: relative; width: 1200px; height: 437px; }

  .card {
    position: absolute; top: 53px;
    width: 509px; height: 291px;
    background: var(--card);
    overflow: hidden;
  }
  .card--front { left: 75px; }
  .card--back { left: 636px; }

  .portrait {
    width: 100%; height: 100%;
    background: radial-gradient(ellipse at 48% 52%, var(--photo-light) 0%, #a9a9a9 45%, var(--photo-dark) 100%);
  }

  .brand { position: absolute; left: 114px; top: 48px; }
  .brand__mark {
    position: absolute; left: 0; top: 0;
    width: 64px; height: 64px; border-radius: 50%;
    background: var(--purple);
  }
  .brand__name {
    position: absolute; left: 74px; top: 18px;
    font-size: 25px; font-weight: 600; letter-spacing: 0.5px;
    text-transform: uppercase; white-space: nowrap;
    color: var(--purple);
  }
  .brand__tagline {
    position: absolute; left: 96px; top: 50px;
    font-size: 8.5px; letter-spacing: 2.4px;
    text-transform: uppercase; white-space: nowrap;
    color: var(--muted);
  }

  .person { position: absolute; left: 16px; top: 168px; }
  .person__name {
    font-size: 21px; line-height: 21px; font-weight: 400;
    color: var(--purple);
  }
  .person__role { margin-top: 6px; font-size: 14.5px; color: var(--muted); }

  .divider {
    position: absolute; left: 221px; top: 178px;
    width: 1px; height: 80px; background: var(--rule);
  }

  .contact { position: absolute; left: 236px; top: 174px; list-style: none; }
  .contact__item {
    display: flex; align-items: center; gap: 6px;
    font-size: 15.5px; line-height: 21px; color: var(--ink);
    white-space: nowrap;
  }
  .contact__icon { width: 11px; height: 11px; fill: var(--ink); flex: none; }

  .card__band {
    position: absolute; left: 0; bottom: 0;
    width: 100%; height: 7px; background: var(--purple-band);
  }
</style>
</head>
<body>
<main class="canvas">
  <section class="card card--front">
    <div class="portrait" role="img" aria-label="Black and white portrait photograph of Lise-Britt, smiling"></div>
  </section>

  <section class="card card--back">
    <div class="brand">
      <span class="brand__mark"></span>
      <span class="brand__name">TealHeron Coaching</span>
      <span class="brand__tagline">Inspirational Leadership</span>
    </div>

    <div class="person">
      <h1 class="person__name">Lise-Britt<br>Holmgaard Pennick</h1>
      <p class="person__role">Leadership Coach and Trainer</p>
    </div>

    <div class="divider"></div>

    <ul class="contact">
      <li class="contact__item">
        <svg class="contact__icon" viewBox="0 0 12 12"><path d="M2.5 1l2 2.2-1 1.2c.7 1.5 1.9 2.7 3.3 3.4l1.2-1L10.5 9l-1.2 1.8C5.4 10.5 1.5 6.6 1 2.4z"/></svg>
        Telephone: +44 1632 960 418
      </li>
      <li class="contact__item">
        <svg class="contact__icon" viewBox="0 0 12 12"><path d="M3 .5h6v11H3zM4 2v6.5h4V2zM5.5 9.5h1v1h-1z" fill-rule="evenodd"/></svg>
        +44 7700 900 562
      </li>
      <li class="contact__item">
        <svg class="contact__icon" viewBox="0 0 12 12"><path d="M.5 2.5h11v7H.5zM1.5 3.3L6 6.6l4.5-3.3v-.1h-9z" fill-rule="evenodd"/></svg>
        lisebritt@tealheroncoaching.example
      </li>
      <li class="contact__item">
        <svg class="contact__icon" viewBox="0 0 12 12"><circle cx="6" cy="6" r="5.2"/><path d="M1 6h10M6 .8c-2 2.8-2 7.6 0 10.4M6 .8c2 2.8 2 7.6 0 10.4" stroke="#fff" stroke-width=".7" fill="none"/></svg>
        www.tealheroncoaching.example
      </li>
    </ul>

    <div class="card__band"></div>
  </section>
</main>
</body>
</html>
```